Support People to improve their image and well-being by provided personalised advise

We need a design for business cards that could be used for production on plato press. We build a new business in our region for advising mostly women (also men though) on style embracing several aspects including fashion, style, self-confidence and ultimately your internal and external image. The business card should be "classy", "french-style". The business is located in the french -speaking part of Switzerland, close to France. The name of the company is Velo Grace

Target Market(s)

Service fees won't be cheap (medium to premium) thus we target mid-class to upper-class women (1st target) and men (2nd target)

Industry/Entity Type

Life Coaching

Contact Information for Business Card

Conseil en Image

+41 79 418 62 07
morinetu@velo-grace.ch
folionet.ch/in/tu-moro-netia

Logo Text

Velo Grace

Colors

Designer to choose colors to be used in the design.

```html
<!DOCTYPE html>
<html lang="en">
<head>
<meta charset="utf-8">
<title>Velo Grace – Business Cards</title>
<link href="https://fonts.googleapis.com/css2?family=Lato:wght@400;700&display=swap" rel="stylesheet">
<style>
  :root {
    --canvas-bg: #e9e6e8;
    --card-light: #ffffff;
    --card-dark: #151515;
    --plum: #7a2a7a;
    --plum-deep: #6e2470;
    --orchid: #a43ca8;
    --magenta-name: #a12aa6;
    --ink: #222222;
    --rule: #8a8a8a;
    --muted: #b8b8b8;
    --accent-dot: #1b7fc2;
  }
  * { margin: 0; padding: 0; box-sizing: border-box; }
  html, body { width: 1200px; height: 900px; overflow: hidden; }
  body {
    background: var(--canvas-bg);
    font-family: "Lato", Arial, sans-serif;
    position: relative;
  }
  .card { position: absolute; box-shadow: 0 6px 18px rgba(0,0,0,0.18); }
  .card-front {
    left: 178px; top: 75px; width: 588px; height: 363px;
    background: var(--card-light);
  }
  .card-back {
    left: 388px; top: 505px; width: 566px; height: 352px;
    background: var(--card-dark);
  }
  .brand-name {
    position: absolute;
    font-weight: 400;
    color: var(--plum);
    white-space: nowrap;
    letter-spacing: 1px;
    line-height: 1;
  }
  .card-front .brand-name { left: 302px; top: 98px; font-size: 50px; }
  .card-back .brand-name { left: 0; width: 100%; text-align: center; top: 118px; font-size: 50px; color: var(--orchid); }
  .accent-bar { position: absolute; left: 0; width: 18px; }
  .accent-bar.name { top: 220px; height: 36px; background: var(--plum-deep); }
  .accent-bar.contact { top: 292px; height: 37px; background: var(--orchid); }
  .person { position: absolute; left: 29px; top: 216px; }
  .person-name { font-weight: 700; font-size: 20px; color: var(--magenta-name); letter-spacing: 0.2px; }
  .person-role { font-size: 16px; color: var(--ink); margin-top: 1px; }
  .contact-list { position: absolute; left: 31px; top: 288px; list-style: none; }
  .contact-list li { display: flex; align-items: center; font-size: 16px; color: var(--ink); height: 22px; }
  .contact-list svg { width: 13px; height: 13px; margin-right: 5px; fill: var(--orchid); }
  .profile-rule { position: absolute; top: 249px; left: 145px; width: 278px; height: 1px; background: var(--rule); }
  .profile-dot {
    position: absolute; top: 236px; left: 271px; width: 27px; height: 27px;
    border-radius: 50%; background: var(--accent-dot); border: 2px solid var(--card-dark);
  }
  .profile-link {
    position: absolute; top: 271px; left: 0; width: 100%; text-align: center;
    font-size: 18px; color: var(--muted);
  }
</style>
</head>
<body>
  <section class="card card-front">
    <div class="brand-name">Velo Grace</div>
    <span class="accent-bar name"></span>
    <div class="person">
      <div class="person-name">JULIEN MARCHAL</div>
      <div class="person-role">Managing Director</div>
    </div>
    <span class="accent-bar contact"></span>
    <ul class="contact-list">
      <li>
        <svg viewBox="0 0 16 16" aria-hidden="true"><path d="M3 1h3l1.5 4-2 1.3a9 9 0 0 0 4.2 4.2L11 8.5l4 1.5v3a2 2 0 0 1-2 2A13 13 0 0 1 1 3a2 2 0 0 1 2-2z"/></svg>
        +41 79 418 62 07
      </li>
      <li>
        <svg viewBox="0 0 16 16" aria-hidden="true"><path d="M1 3h14v10H1z"/><path d="M2.5 4.5 8 9l5.5-4.5" stroke="#fff" stroke-width="1.4" fill="none"/></svg>
        morinetu@velo-grace.ch
      </li>
    </ul>
  </section>

  <section class="card card-back">
    <div class="brand-name">Velo Grace</div>
    <span class="profile-rule"></span>
    <span class="profile-dot"></span>
    <div class="profile-link">folionet.ch/in/tu-moro-netia</div>
  </section>
</body>
</html>
```